Corvimo Business Card

Corvimo is a young and energetic software development consultancy. We spend our time on the road working with clients on their sites an meeting new potential customers and employees!

We need a sharp, vibrant and memorable business card that will inspires those that receive it to look after it as it oozes quality and is a nice thing in its own right.

We like bold colours and distinctive design. So show us what you can do.

In terms of information on the card, it would be good to see:

* Our logo (Obviously :) )
* Employee name
* Email
* Website address
* Mobile number
* Full company name (Corvimo ltd)
* Registered company number
* Registered company address

Industry/Entity Type

Software

Requirements
Nice to have
• We are thinking that having a QR Code on the business card could be a good way of adding active marketing. It would be good to see if you are able to merge the kind of element in to your designs!

Maybe something special could be achieved using a visual QR Code like those produced at http://www.pixoranta.example/ ? You have our media so feel free to have a play.

```html
<!DOCTYPE html>
<html lang="en">
<head>
<meta charset="utf-8">
<title>Corvimo Business Card</title>
<link href="https://fonts.googleapis.com/css2?family=Cormorant+SC:wght@500&family=Lato:wght@400&display=swap" rel="stylesheet">
<style>
  :root {
    --backdrop: #e4e2df;
    --card-white: #f7f7f6;
    --brand-red: #b50f12;
    --logo-red: #cf2a3a;
    --panel-grey: #bababa;
    --panel-text: #f4f4f4;
    --divider: #eeeeee;
  }
  * { margin: 0; padding: 0; box-sizing: border-box; }
  html, body {
    width: 1200px;
    height: 900px;
    overflow: hidden;
    background: var(--backdrop);
  }
  .canvas {
    position: relative;
    width: 1200px;
    height: 900px;
  }
  .card {
    position: absolute;
    left: 120px;
    top: 176px;
    width: 960px;
    height: 548px;
    background: var(--card-white);
    display: grid;
    grid-template-columns: 518px 1fr;
    box-shadow: 0 10px 30px rgba(0,0,0,0.15);
  }
  .brand-side {
    position: relative;
  }
  .wordmark {
    position: absolute;
    left: 62px;
    top: 350px;
    font-family: "Lato", sans-serif;
    font-weight: 400;
    font-size: 66px;
    letter-spacing: 2px;
    color: var(--logo-red);
    white-space: nowrap;
  }
  .info-side {
    display: grid;
    grid-template-rows: 148px 8px 1fr;
  }
  .identity {
    background: var(--brand-red);
    padding: 62px 0 0 44px;
    color: #ffffff;
  }
  .person-name {
    font-family: "Cormorant SC", serif;
    font-weight: 500;
    font-size: 36px;
    line-height: 1;
    letter-spacing: 1px;
  }
  .person-role {
    font-family: "Lato", sans-serif;
    font-size: 19px;
    margin-top: 6px;
  }
  .divider { background: var(--divider); }
  .contact {
    background: var(--panel-grey);
    padding: 40px 0 0 44px;
    font-family: "Lato", sans-serif;
    font-size: 19px;
    line-height: 26px;
    color: var(--panel-text);
    white-space: nowrap;
  }
  .postal { font-style: normal; }
  .contact-row { display: flex; }
  .contact-label { width: 58px; }
  .online { margin-top: 30px; }
</style>
</head>
<body>
<main class="canvas">
  <article class="card">
    <section class="brand-side">
      <div class="wordmark">CORVIMO</div>
    </section>
    <section class="info-side">
      <header class="identity">
        <div class="person-name">John E. Doe</div>
        <div class="person-role">Managing Director</div>
      </header>
      <div class="divider"></div>
      <div class="contact">
        <address class="postal">
          <div>67210, Ashcombe Street</div>
          <div>472 KRM Fenwick Road, UK</div>
        </address>
        <div class="contact-row"><span class="contact-label">tel.:</span><span>+44 16 404 271</span></div>
        <div class="contact-row"><span class="contact-label">fax:</span><span>+44 73 612 908</span></div>
        <div class="online">
          <div>www.corvimo.co.uk</div>
          <div>john.doe@corvimo.co.uk</div>
        </div>
      </div>
    </section>
  </article>
</main>
</body>
</html>
```